Website for Meadowlark Harvest Co

Slogan to be used is Fresh is Best !
I would like the website to be like my other business @ www.tuberworks.com.au. It is the same business

Vegetable Processing

Coded - Design and coding required

1 page

```html
<!DOCTYPE html>
<html lang="en">
<head>
<meta charset="utf-8">
<title>Meadowlark Harvest Co – Fresh is Best</title>
<link rel="stylesheet" href="https://fonts.googleapis.com/css2?family=Lato:wght@400;700&family=Playfair+Display:ital,wght@0,400;0,700;0,900;1,700&display=swap">
<style>
  :root {
    --lime: #8cb828;
    --leaf: #6d9a4b;
    --brand: #7ea22a;
    --ink: #1d1d1d;
    --white: #ffffff;
    --hero-dark: #2b231d;
    --hero-mid: #5a3f2a;
  }
  * { margin: 0; padding: 0; box-sizing: border-box; }
  html, body { width: 1200px; height: 793px; overflow: hidden; }
  body { position: relative; font-family: "Lato", sans-serif; background: var(--white); }

  .promo-bar {
    position: absolute; left: 0; top: 0; width: 1200px; height: 38px;
    background: var(--lime);
    display: flex; align-items: center; justify-content: center;
    font-family: "Playfair Display", serif; font-style: italic; font-weight: 700;
    font-size: 13px; color: var(--white);
  }

  .site-header {
    position: absolute; left: 0; top: 38px; width: 1200px; height: 50px;
    background: var(--white);
  }
  .brand-name {
    position: absolute; left: 162px; top: 0; height: 50px;
    display: flex; align-items: center; white-space: nowrap;
    font-family: "Playfair Display", serif; font-weight: 400;
    font-size: 24px; color: var(--brand);
  }
  .main-nav {
    position: absolute; left: 432px; top: 0; height: 50px;
    display: flex; align-items: center; gap: 18px; white-space: nowrap;
    font-size: 10px; font-weight: 700; text-transform: uppercase; color: var(--ink);
  }
  .main-nav .active { color: var(--brand); }
  .call-box { position: absolute; left: 884px; top: 8px; height: 34px; }
  .call-icon { position: absolute; left: 0; top: 0; }
  .call-label { position: absolute; left: 41px; top: 1px; font-size: 12px; color: var(--ink); white-space: nowrap; }
  .call-number {
    position: absolute; left: 41px; top: 13px; white-space: nowrap;
    font-family: "Playfair Display", serif; font-weight: 700; font-size: 20px; color: var(--brand);
  }

  .product-bar {
    position: absolute; left: 0; top: 88px; width: 1200px; height: 37px;
    background: var(--leaf);
    display: flex; align-items: center; justify-content: center;
    font-family: "Playfair Display", serif; font-weight: 700; font-size: 10px;
    color: var(--white); text-transform: uppercase; letter-spacing: 0.2px;
  }
  .product-bar span + span::before {
    content: "|"; font-family: "Lato", sans-serif; font-weight: 400;
    margin: 0 10px; opacity: 0.8;
  }

  .hero {
    position: absolute; left: 0; top: 125px; width: 1200px; height: 668px;
    overflow: hidden;
  }
  .hero-photo {
    position: absolute; inset: 0;
    background:
      radial-gradient(ellipse 48% 55% at 52% 52%, #7a4a2a 0%, rgba(90,55,35,0.6) 45%, transparent 75%),
      radial-gradient(ellipse 30% 30% at 20% 70%, rgba(140,60,30,0.7), transparent 70%),
      radial-gradient(ellipse 30% 30% at 82% 70%, rgba(160,70,25,0.6), transparent 70%),
      linear-gradient(180deg, var(--hero-dark) 0%, var(--hero-mid) 55%, #3a2d24 100%);
  }
  .slogan {
    position: absolute; left: 0; top: 190px; width: 1200px; text-align: center;
    font-family: "Playfair Display", serif; font-weight: 900;
    font-size: 156px; line-height: 170px; letter-spacing: -3px; color: var(--white);
  }
  .site-footer {
    position: absolute; left: 0; top: 631px; width: 1200px; text-align: center;
    font-size: 10px; color: var(--white);
  }
  .site-footer .sep { margin: 0 12px; }
</style>
</head>
<body>
  <div class="promo-bar">You can place your order over the phone. easy!</div>

  <header class="site-header">
    <div class="brand-name">Meadowlark Harvest Co</div>
    <nav class="main-nav">
      <span class="active">Home</span>
      <span>Our Customers</span>
      <span>Why Choose Us</span>
      <span>About Meadowlark</span>
      <span>Contact Us</span>
    </nav>
    <div class="call-box">
      <svg class="call-icon" width="34" height="34" viewBox="0 0 34 34" aria-hidden="true">
        <circle cx="17" cy="17" r="17" fill="#7ea22a"/>
        <path d="M12.5 10.5c.6-.6 1.5-.5 2 .1l1.6 2.1c.4.5.4 1.2 0 1.7l-.9 1c.7 1.5 1.9 2.7 3.4 3.4l1-.9c.5-.4 1.2-.4 1.7 0l2.1 1.6c.6.5.7 1.4.1 2l-1 1c-.9.9-2.3 1.1-3.4.5-3-1.6-5.4-4-7-7-.6-1.1-.4-2.5.5-3.4z" fill="#fff"/>
      </svg>
      <div class="call-label">Call us now</div>
      <div class="call-number">02 5550 1846</div>
    </div>
  </header>

  <nav class="product-bar">
    <span>Potatoes</span><span>Pumpkin</span><span>Carrot</span><span>Onion</span><span>Cabbage</span><span>Celery</span><span>Capsicum</span><span>Zucchini</span><span>Mushroom</span><span>Spinach</span><span>Brocolli</span><span>Cauliflower</span><span>Mixes</span>
  </nav>

  <section class="hero">
    <div class="hero-photo" role="img" aria-label="Wicker basket of fresh vegetables and fruit on a rustic wooden table"></div>
    <h1 class="slogan">Fresh is Best !</h1>
    <footer class="site-footer">© copyrights 2023 Meadowlark Harvest Co<span class="sep">|</span>All rights reserved.</footer>
  </section>
</body>
</html>
```